Lantern - Web Design Project

We are seeking to have our website redesigned. Our current webpage is rather dated looking www.lantern-outcomes.com We will be utilizing similar content to explain our services as what is in the website now. We do not see it at a retail portal but rather a website for those inquiring about our services as a reference check so to speak.

We wish to have a look that is considered clean, fresh, contemporary and contains a business savvy vibe.

We prefer isolated white background and also wish to retain the integrity of our Logo and colour scheme.

We are looking for something that doesnt look like it was designed at home on sitemoose. We are hoping to find something that looks like it would reside on a tablet.
Updates

Hello designers!

We apologize for our tardiness as we have been quite preoccupied. We will be extending our invites to the end of January!

Hello All,

Please review our offer once again for updated requirements.  We are hoping to accept a design by months end.

Lantern

Target Market(s)

Business to business clients and Large manufacturers

Industry/Entity Type

Retail

Requirements
Must have
• Existing Logo

There must be an area dedicated to an intro video that will be incorporated on our landing page.

We require design of the other pages as well not only the landing page.

```html
<!DOCTYPE html>
<html lang="en">
<head>
<meta charset="utf-8">
<title>Lantern Performance</title>
<link rel="stylesheet" href="https://fonts.googleapis.com/css2?family=Ubuntu:ital,wght@0,400;0,500;0,700;1,400&family=Roboto+Condensed:wght@700&family=Oswald:wght@600;700&display=swap">
<style>
:root{
  --red:#e31b1b;
  --dark-red:#b50f0f;
  --ink:#3a3a3a;
  --grey-text:#555;
  --footer-bg:#3b3b3b;
  --footer-text:#d8d8d8;
  --white:#fff;
  --page:#f4f4f4;
}
*{margin:0;padding:0;box-sizing:border-box}
html,body{width:1045px;height:1200px;overflow:hidden;background:var(--white)}
body{font-family:"Ubuntu",sans-serif;color:var(--ink);position:relative}
.site-header{position:absolute;top:0;left:0;width:1045px;height:86px;background:linear-gradient(#eef0f2,#dfe2e6);border-bottom:4px solid var(--red)}
.brand{position:absolute;left:122px;top:18px;display:flex;align-items:center;gap:8px}
.brand-dot{width:14px;height:14px;border-radius:50%;background:var(--red)}
.brand-name{font-family:"Ubuntu",sans-serif;font-weight:500;font-size:44px;color:#555;line-height:1}
.utility{position:absolute;top:8px;left:796px;display:flex;gap:5px}
.utility a{font-size:11px;color:var(--white);text-decoration:none;padding:3px 8px;height:19px;display:block}
.btn-signin{background:var(--red)}
.btn-language{background:#444}
.main-nav{position:absolute;top:50px;left:266px;display:flex;height:36px}
.main-nav a{font-family:"Roboto Condensed",sans-serif;font-weight:700;font-size:12px;color:#111;text-decoration:none;padding:0 16px;line-height:36px;text-transform:uppercase}
.main-nav a.active{background:var(--red);color:var(--white);padding:0 12px}
.hero{position:absolute;top:90px;left:0;width:1045px;height:408px;background:linear-gradient(120deg,#2a2012 0%,#6b4a24 35%,#c58a32 60%,#f0c060 75%,#5a4a30 100%)}
.hero-rule{position:absolute;top:498px;left:0;width:1045px;height:4px;background:var(--red)}
.hero-arrow{position:absolute;top:185px;width:40px;height:40px}
.hero-arrow.prev{left:122px}.hero-arrow.next{left:883px}
.content{position:absolute;top:502px;left:0;width:1045px;height:431px;background:linear-gradient(#ececec,#fff 80px)}
.divider{position:absolute;left:648px;top:10px;width:14px;height:410px;background:linear-gradient(90deg,rgba(0,0,0,.06),rgba(0,0,0,0))}
.welcome{position:absolute;left:123px;top:40px;width:500px}
.welcome h2{font-weight:400;font-size:21px;color:#444;line-height:1.1}
.welcome h1{font-weight:400;font-size:27px;color:var(--red);line-height:1.3;margin-bottom:20px}
.welcome p{font-size:11.4px;line-height:16.5px;color:var(--grey-text);margin-bottom:16px}
.emergency{position:absolute;left:706px;top:36px;width:194px}
.emergency-title{font-family:"Oswald",sans-serif;font-weight:700;font-size:31px;color:#111;text-align:center;line-height:1}
.emergency-ribbon{display:block;margin-top:-2px}
.contact{position:absolute;left:706px;top:130px;width:240px}
.contact h3{font-weight:500;font-size:16px;color:#111;margin-bottom:10px}
.contact h3 span{color:var(--red)}
.contact li{list-style:none;font-size:11.4px;color:#222;display:flex;align-items:center;gap:10px;height:23px}
.map{margin-top:14px;width:191px;height:77px;border:3px solid #ddd;border-radius:3px;background:linear-gradient(135deg,#e8efe0,#d7e4cd 50%,#eee8d8);box-shadow:0 2px 3px rgba(0,0,0,.25)}
.site-footer{position:absolute;top:933px;left:0;width:1045px;height:201px;background:var(--footer-bg);color:var(--footer-text)}
.site-footer h4{font-weight:400;font-size:16px;color:var(--white);margin-bottom:12px}
.testimonial{position:absolute;left:123px;top:30px;width:200px;font-size:11px;line-height:16px}
.testimonial cite{display:block;margin-top:14px;font-style:italic;color:var(--white)}
.quick-links{position:absolute;left:379px;top:30px;width:270px}
.quick-links ul{display:grid;grid-template-columns:132px 132px;row-gap:5px;list-style:none;padding-left:2px}
.quick-links a{font-size:11px;color:var(--footer-text);text-decoration:none}
.newsletter{position:absolute;left:673px;top:30px;width:240px}
.newsletter h4{font-size:15px;margin-bottom:6px}
.newsletter p{font-size:10.5px;line-height:15px}
.signup{display:flex;margin-top:12px;border:2px solid var(--white);width:232px;height:29px}
.signup span{flex:1;background:var(--white);color:#444;font-size:10.5px;padding:6px 6px}
.signup button{background:var(--red);color:var(--white);border:0;font-family:"Ubuntu",sans-serif;font-weight:700;font-size:12px;width:56px}
.questions{margin-top:10px;font-size:13px;color:#bbb}
.questions strong{display:block;font-size:17px;color:var(--white);font-weight:500}
.copyright{position:absolute;top:1153px;left:0;width:1045px;text-align:center;font-size:10.5px;color:#777}
.social{position:absolute;top:1174px;left:498px;display:flex;gap:4px}
.social span{width:13px;height:13px;background:#3b6aa0;border-radius:2px}
</style>
</head>
<body>
<header class="site-header">
  <div class="brand"><span class="brand-dot"></span><span class="brand-name">lantern</span></div>
  <div class="utility"><a class="btn-signin" href="#">Sign In</a><a class="btn-language" href="#">Language ⊙</a></div>
  <nav class="main-nav">
    <a class="active" href="#">Home</a><a href="#">Who We Are</a><a href="#">Cross the Lantern</a><a href="#">Performance Solutions</a><a href="#">Sustain Solutions</a><a href="#">Join Us</a>
  </nav>
</header>

<section class="hero" role="img" aria-label="Night photograph of a city bridge with red steel girders and light trails of traffic">
  <svg class="hero-arrow prev" viewBox="0 0 40 40"><circle cx="20" cy="20" r="19" fill="#fff"/><path d="M23 11l-9 9 9 9" fill="none" stroke="#222" stroke-width="4"/></svg>
  <svg class="hero-arrow next" viewBox="0 0 40 40"><circle cx="20" cy="20" r="19" fill="#fff"/><path d="M17 11l9 9-9 9" fill="none" stroke="#222" stroke-width="4"/></svg>
</section>
<div class="hero-rule"></div>

<main class="content">
  <div class="divider"></div>
  <article class="welcome">
    <h2>WELCOME TO</h2>
    <h1>LANTERN PERFORMANCE</h1>
    <p>Lorem Ipsum is simply dummy text of the printing and typesetting industry. Lorem Ipsum has been the industry's standard dummy text ever since the 1500s.When an unknown printer took a galley of type and scrambled it to make a type specimen book.</p>
    <p>It has survived not only five centuries, but also the leap into electronic typesetting, remaining essentially unchanged.</p>
    <p>Lorem Ipsum is simply dummy text of the printing and typesetting industry. Lorem Ipsum has been the industry's standard dummy text ever since the 1500s.When an unknown printer took a galley of type and scrambled it to make a type specimen book.</p>
    <p>It has survived not only five centuries, but also the leap into electronic typesetting, remaining essentially unchanged.</p>
  </article>

  <aside>
    <div class="emergency">
      <div class="emergency-title">24 HOUR</div>
      <svg class="emergency-ribbon" width="194" height="70" viewBox="0 0 194 70">
        <defs><linearGradient id="shade" x1="0" y1="0" x2="0" y2="1"><stop offset="0" stop-color="#ddd"/><stop offset="1" stop-color="#fff"/></linearGradient></defs>
        <rect x="2" y="30" width="190" height="40" fill="url(#shade)"/>
        <path d="M12 0h170v30l12 3-97 26L0 33l12-3z" fill="var(--red)"/>
        <path d="M0 33l12-3v6zM194 33l-12-3v6z" fill="var(--dark-red)"/>
        <text x="97" y="20" text-anchor="middle" font-family="Ubuntu,sans-serif" font-weight="500" font-size="16" fill="#fff">EMERGENCY</text>
        <text x="97" y="40" text-anchor="middle" font-family="Ubuntu,sans-serif" font-weight="500" font-size="16" fill="#fff">SERVICE!</text>
      </svg>
    </div>
    <div class="contact">
      <h3>CONTACT <span>INFO</span></h3>
      <ul>
        <li><svg width="13" height="13" viewBox="0 0 13 13"><path d="M2 1l3 0 1 3-2 1.5a7 7 0 0 0 3.5 3.5L9 7l3 1v3c-6 1-11-4-10-10z" fill="var(--red)"/></svg>Phone: +1.888.555.0142</li>
        <li><svg width="13" height="13" viewBox="0 0 13 13"><rect x="0" y="2" width="13" height="9" fill="var(--red)"/><path d="M0 2l6.5 5L13 2" fill="none" stroke="#fff"/></svg>Email:info@lantern-outcomes.com</li>
        <li><svg width="13" height="13" viewBox="0 0 13 13"><circle cx="6.5" cy="4" r="3" fill="var(--red)"/><path d="M1 13c0-4 2.5-6 5.5-6S12 9 12 13z" fill="var(--red)"/></svg>Everyday: 07:00AM to 05:00PM</li>
      </ul>
      <div class="map" role="img" aria-label="Small road map showing the office location"></div>
    </div>
  </aside>
</main>

<footer class="site-footer">
  <div class="testimonial">
    <h4>Testimonials</h4>
    <p>"Lorem Ipsum is simply dummy text of the printing and typesetting industry. Lorem Ipsum has been the industry's standard dummy text ever since the 1500s."</p>
    <cite>- Maren Colby</cite>
  </div>
  <div class="quick-links">
    <h4>Quick Links</h4>
    <ul>
      <li><a href="#">Home</a></li><li><a href="#">Performance Solutions</a></li>
      <li><a href="#">Who We Are</a></li><li><a href="#">Sustain Solutions</a></li>
      <li><a href="#">Cross The Lantern</a></li><li><a href="#">Join Us</a></li>
    </ul>
  </div>
  <div class="newsletter">
    <h4>Sign Up For Our Newsletter</h4>
    <p>Sign up to receive special offers and promotions.</p>
    <div class="signup"><span>Enter your email address</span><button>SUBMIT</button></div>
    <div class="questions">Questions? Call<strong>1.888.555.0142</strong></div>
  </div>
</footer>

<p class="copyright">Copyright © 2012 Lantern Performance. All Rights Reserved.</p>
<div class="social"><span></span><span></span><span></span></div>
</body>
</html>
```